Business card for communications

Need a business card for my consulting business - I work with not for profits, start ups and social enterprises on their media, communications campaigns.

Please see my website for colours, images and fonts www.morvenquillet.example

Morven Quillet
Communications & Campaign strategist
Sydney - Melbourne
M: 0498 317 250
E: morven@morvenquillet.example
S: morvenquillet
W: morvenquillet.example
T: @morvenquillet

(above is info only and can be presented any way e.g. should not have to be M for mobile - it should be an icon)
Updates

Dear designers I have updated the brief and uploaded high res images from my website for you to use. The designs so far with the use of images and icons are much better so far. Thank you I look forward to receiving your revised designs. Morven Quillet

Industry/Entity Type

Communications

Font styles to use
Sans Serif

Requirements
Must have
• Icons for contact details
Images from the website www.morvenquillet.example
Nice to have
• Images - attached

```html
<!DOCTYPE html>
<html lang="en">
<head>
<meta charset="utf-8">
<title>Morven Quillet – Business Card</title>
<link href="https://fonts.googleapis.com/css2?family=Montserrat:wght@600;700&family=Open+Sans:wght@400;600&display=swap" rel="stylesheet">
<style>
  :root {
    --backdrop: #3b3b3d;
    --card-white: #ffffff;
    --brand-yellow: #fff200;
    --ink: #1d1d1b;
    --ink-soft: #4a4a4a;
    --photo-warm: #a0713f;
    --photo-light: #d9c3a0;
  }
  * { margin: 0; padding: 0; box-sizing: border-box; }
  html, body { width: 1200px; height: 746px; overflow: hidden; }
  body {
    background: var(--backdrop);
    position: relative;
    font-family: "Open Sans", sans-serif;
    color: var(--ink);
  }
  .card {
    position: absolute;
    top: 223px;
    width: 520px;
    height: 300px;
    border-radius: 16px;
    overflow: hidden;
    background: var(--card-white);
  }
  .card--front { left: 50px; }
  .card--back { left: 630px; }

  /* Front */
  .front-band { position: absolute; inset: 0; width: 100%; height: 100%; }
  .profile { position: absolute; left: 30px; top: 92px; display: flex; align-items: center; gap: 12px; }
  .profile__portrait {
    width: 72px; height: 72px; border-radius: 10px; flex: none;
    background: linear-gradient(160deg, #8c8a86, #5b4a40);
  }
  .profile__name {
    font-family: "Montserrat", sans-serif; font-weight: 700;
    font-size: 17px; letter-spacing: 0.4px; text-transform: uppercase; line-height: 1.1;
    white-space: nowrap;
  }
  .profile__location { font-size: 10.5px; color: var(--ink-soft); margin-top: 2px; white-space: nowrap; }

  .contact-list { position: absolute; left: 300px; top: 30px; list-style: none; }
  .contact-list__item { display: flex; align-items: center; gap: 7px; height: 26px; font-size: 11.5px; white-space: nowrap; }
  .contact-list__icon { width: 20px; height: 20px; flex: none; }

  .services { position: absolute; font-family: "Open Sans", sans-serif; font-weight: 600; font-size: 13px; text-transform: uppercase; line-height: 1.3; }
  .services--main { left: 40px; top: 238px; }
  .services--media { left: 218px; top: 198px; }
  .services__divider { position: absolute; left: 206px; top: 196px; width: 1.5px; height: 30px; background: var(--ink); }

  /* Back */
  .back-photo {
    position: absolute; left: 0; top: 0; width: 100%; height: 212px;
    background: linear-gradient(135deg, var(--photo-light) 0%, var(--photo-warm) 45%, #7a5430 100%);
  }
  .back-band {
    position: absolute; left: 0; top: 212px; width: 100%; height: 88px;
    background: var(--brand-yellow);
    display: flex; align-items: center; padding-left: 40px;
  }
  .back-band__name {
    font-family: "Montserrat", sans-serif; font-weight: 700;
    font-size: 30px; letter-spacing: 1px; text-transform: uppercase;
  }
</style>
</head>
<body>

<section class="card card--front" aria-label="Card front">
  <svg class="front-band" viewBox="0 0 520 300" preserveAspectRatio="none" aria-hidden="true">
    <polygon points="0,215 520,160 520,300 0,300" fill="var(--brand-yellow)"/>
  </svg>

  <div class="profile">
    <div class="profile__portrait" role="img" aria-label="Portrait photo of Morven Quillet"></div>
    <div>
      <div class="profile__name">Morven Quillet</div>
      <div class="profile__location">Sydney - Melbourne</div>
    </div>
  </div>

  <ul class="contact-list">
    <li class="contact-list__item">
      <svg class="contact-list__icon" viewBox="0 0 20 20" aria-hidden="true">
        <circle cx="10" cy="10" r="10" fill="var(--brand-yellow)"/>
        <path d="M6.2 5.2l2 0 1 2.6-1.3 1a6 6 0 0 0 3.3 3.3l1-1.3 2.6 1 0 2a1.2 1.2 0 0 1-1.3 1.2A9 9 0 0 1 5 6.5a1.2 1.2 0 0 1 1.2-1.3z" fill="var(--ink)"/>
      </svg>
      <span>0498 317 250</span>
    </li>
    <li class="contact-list__item">
      <svg class="contact-list__icon" viewBox="0 0 20 20" aria-hidden="true">
        <circle cx="10" cy="10" r="10" fill="var(--brand-yellow)"/>
        <rect x="4.5" y="6.5" width="11" height="7.5" fill="none" stroke="var(--ink)" stroke-width="1.4"/>
        <polyline points="4.5,6.5 10,11 15.5,6.5" fill="none" stroke="var(--ink)" stroke-width="1.4"/>
      </svg>
      <span>morven@morvenquillet.example</span>
    </li>
    <li class="contact-list__item">
      <svg class="contact-list__icon" viewBox="0 0 20 20" aria-hidden="true">
        <circle cx="10" cy="10" r="10" fill="var(--brand-yellow)"/>
        <path d="M5 6h10v6.5H9l-3 2.5v-2.5H5z" fill="none" stroke="var(--ink)" stroke-width="1.4" stroke-linejoin="round"/>
      </svg>
      <span>morvenquillet</span>
    </li>
    <li class="contact-list__item">
      <svg class="contact-list__icon" viewBox="0 0 20 20" aria-hidden="true">
        <circle cx="10" cy="10" r="10" fill="var(--brand-yellow)"/>
        <text x="10" y="14.2" text-anchor="middle" font-family="Open Sans, sans-serif" font-weight="600" font-size="12" fill="var(--ink)">@</text>
      </svg>
      <span>morvenquillet.example</span>
    </li>
    <li class="contact-list__item">
      <svg class="contact-list__icon" viewBox="0 0 20 20" aria-hidden="true">
        <circle cx="10" cy="10" r="10" fill="var(--brand-yellow)"/>
        <circle cx="10" cy="7.6" r="2.6" fill="var(--ink)"/>
        <path d="M5 15a5 4 0 0 1 10 0z" fill="var(--ink)"/>
      </svg>
      <span>@morvenquillet</span>
    </li>
  </ul>

  <p class="services services--main">Communications<br>Strategy</p>
  <span class="services__divider" aria-hidden="true"></span>
  <p class="services services--media">Media</p>
</section>

<section class="card card--back" aria-label="Card back">
  <div class="back-photo" role="img" aria-label="Overhead photo of a team working around a wooden desk with laptops, papers and coffee"></div>
  <div class="back-band">
    <span class="back-band__name">Morven Quillet</span>
  </div>
</section>

</body>
</html>
```